Brochure for luxury baby clothing

We need a square (5.5') catalog/brochure to market our baby clothing to baby stores. We offer baby clothing made of 100% peruvian pima cotton, world's finest and softest cotton. The online store was launched 2 months ago in Canada and we are now going to market the clothing to stores across Canada. We are looking to have a beautiful catalog to present the products to potential buyers (store owners and managers)
Catalog will be presented in print but we may also use a table to present it
Selected designer to provide source document (illustrator)

Target Market(s)

Baby stores and department stores across Canada (store owners, buyers and managers)

Industry/Entity Type

Baby

Requirements
Must have
• - Cover
• - Pages 2 – 3. About us section
• o 2: Nice image resembling softness, exclusive, luxury, cozy... and perhaps a phase: "Pure softness for babies..."
• o 3: About Velloro Kids Canada and about Pima Cotton (content in our website: www.vellorokids.ca)
• - Pages 4-5: Newborn section. Picture of a baby wearing our clothing and pictures and short descriptions of some products
• - Pages 6-7: Girls section. Picture of a girl wearing our clothing and pictures and short descriptions of some products
• - Pages 8-9: Boys section. Picture of a boy wearing our clothing and pictures and short descriptions of some products
• - Page 10. Organics section. Pictures and short descriptions of some products
• - Page 11. Accessories. Pictures and short descriptions of some products
• - Back. Logo and contact information (email, phone, facebook, Instagram)

```html
<!DOCTYPE html>
<html lang="en">
<head>
<meta charset="utf-8">
<title>Velloro Kids Canada – About Us Spread</title>
<link href="https://fonts.googleapis.com/css2?family=Cabin:ital,wght@0,400;0,500;1,400&display=swap" rel="stylesheet">
<style>
  :root {
    --stage: #ece8e2;
    --panel-taupe: #7b7062;
    --title-blue: #a9c8e6;
    --body-cream: #f3efe6;
    --headline-white: #ffffff;
    --fur-white: #f4f5f6;
    --hood-grey: #6f7378;
    --hood-dark: #4e5256;
    --knit-grey: #c9cbc6;
    --cheek-warm: #ecd9cc;
    --snow: #fbfcfd;
    --sheet-light: #fdf9ef;
    --sheet-cream: #f3e6cb;
    --sheet-gold: #e4cc9f;
    --hair-gold: #e6c48e;
  }
  * { box-sizing: border-box; margin: 0; padding: 0; }
  html, body { width: 1200px; height: 880px; overflow: hidden; }
  body {
    background: var(--stage);
    font-family: "Cabin", "Segoe UI", sans-serif;
    display: flex;
    align-items: center;
    justify-content: center;
  }
  .spread {
    width: 1120px;
    height: 560px;
    display: flex;
    box-shadow: 0 6px 22px rgba(0,0,0,0.18);
  }
  .page { width: 560px; height: 560px; position: relative; overflow: hidden; }

  /* Left page: full-bleed winter hood photo */
  .page--intro .hero-photo {
    position: absolute; inset: 0;
    background:
      radial-gradient(ellipse 20% 16% at 47% 64%, var(--cheek-warm) 0%, rgba(236,217,204,0) 100%),
      radial-gradient(ellipse 24% 20% at 46% 36%, var(--knit-grey) 0%, rgba(201,203,198,0) 100%),
      radial-gradient(ellipse 44% 40% at 48% 55%, var(--fur-white) 0%, rgba(244,245,246,0.85) 55%, rgba(244,245,246,0) 100%),
      linear-gradient(to top, var(--snow) 0%, rgba(251,252,253,0.9) 12%, rgba(251,252,253,0) 30%),
      radial-gradient(ellipse 30% 35% at 82% 62%, var(--hood-dark) 0%, rgba(78,82,86,0) 100%),
      radial-gradient(ellipse 26% 30% at 12% 70%, var(--hood-grey) 0%, rgba(111,115,120,0) 100%),
      linear-gradient(180deg, #d9dadc 0%, #a6a9ad 45%, #8d9095 100%);
  }
  .page--intro .tagline {
    position: absolute;
    top: 78px; left: 190px;
    color: var(--headline-white);
    font-style: italic;
    font-size: 22px;
    letter-spacing: 0.4px;
    transform: rotate(9deg);
    transform-origin: left center;
    text-shadow: 0 1px 3px rgba(0,0,0,0.3);
    white-space: nowrap;
  }

  /* Right page: sleeping-baby photo strip + text panel */
  .page--about { display: flex; }
  .about-photo {
    width: 48%;
    height: 100%;
    background:
      radial-gradient(ellipse 34% 16% at 40% 12%, var(--hair-gold) 0%, rgba(230,196,142,0) 100%),
      radial-gradient(ellipse 60% 30% at 55% 40%, #fffaf0 0%, rgba(255,250,240,0) 100%),
      radial-gradient(ellipse 70% 40% at 35% 78%, var(--sheet-light) 0%, rgba(253,249,239,0) 100%),
      linear-gradient(160deg, var(--sheet-cream) 0%, var(--sheet-light) 40%, var(--sheet-cream) 70%, var(--sheet-gold) 100%);
  }
  .about-panel {
    width: 52%;
    height: 100%;
    background: var(--panel-taupe);
    color: var(--body-cream);
    padding: 30px 22px 24px 24px;
    font-size: 12px;
    line-height: 1.28;
  }
  .about-panel h2 {
    color: var(--title-blue);
    font-weight: 400;
    font-size: 15px;
    margin-bottom: 8px;
  }
  .about-panel p { text-align: justify; margin-bottom: 11px; }
  .about-panel .locations-label { text-align: left; margin-bottom: 1px; }
  .location-list { list-style: disc; padding-left: 16px; margin-bottom: 11px; }
  .location-list li.more { list-style: none; margin-left: -6px; }
  .about-panel .network { text-align: left; }
</style>
</head>
<body>
  <main class="spread">
    <section class="page page--intro">
      <div class="hero-photo" role="img" aria-label="Smiling baby in a knitted hat and white fur-trimmed winter hood"></div>
      <p class="tagline">Pure softness for babies...</p>
    </section>

    <section class="page page--about">
      <div class="about-photo" role="img" aria-label="Baby sleeping peacefully on soft cream pima cotton sheets"></div>
      <div class="about-panel">
        <h2>Velloro Kids Canada</h2>
        <p>Velloro Kids is a Peruvian company that was born in 2010. A dream of two friends who once had the wonderful experience of becoming mothers. The magic of motherhood gave them the desire to want the best for their babies. Using classic designs and the softest pima cotton they created Velloro Kids, a growing recognized brand.</p>
        <p>At Velloro Kids we care about providing our customers with the highest quality apparel using the finest, softest and most appreciated type of cotton in the world. From northern Peru we create exclusives designs that makes our product unique. We guarantee the quality and comfort that your baby deserves.</p>
        <p class="locations-label">We are located in:</p>
        <ul class="location-list">
          <li>Toronto-Canada</li>
          <li>Lima-Peru</li>
          <li>São Paulo- Brazil</li>
          <li>Miami-United States</li>
          <li class="more">and more coming soon!</li>
        </ul>
        <p class="network">Plus an exclusive multi-client network that carry our products worldwide and representatives in Europe.</p>
      </div>
    </section>
  </main>
</body>
</html>
```